MoveNest Landing Page

We need to freshen up our homepage.

The company is MoveNest.com. We provide cloud-based management software for class venues - dance, yoga, martial arts, etc.

The challenge here is to create something that's simultaneously lighthearted and professional. We want our customers to know that the software is easy, fun and non-intimidating, but also powerful enough to handle whatever they throw at it.

Page content can remain the same as it is now. Feel free to move things around, manipulate it however you like.

We like our logo, but feel free to manipulate it as part of your design. Fonts used in the logo are Futura Extra Bold and Rockwell.

NOTE: The default screenshot in the homepage video is NOT our branding choice, it just happens to be the default freeze frame from vidloop.. Feel free to ignore it altogether in your design. We are not affiliated with that character, or the app that we used to create the vid.
Updates

Project Deadline Extended
Reason: We are extending this contest by request. Out of 65 designs, so far we only really like 4. There's still a good chance to win this contract! Please submit your very best :) Owen

Target Market(s)

Studio owners who are not necessarily tech savvy.

Industry/Entity Type

Software

Requirements
Must have
• Look and feel of a modern web app.

Delivery in a layered PSD.

```html
<!DOCTYPE html>
<html lang="en">
<head>
<meta charset="utf-8">
<title>MoveNest – Manage your classes</title>
<link rel="stylesheet" href="https://fonts.googleapis.com/css2?family=Roboto+Slab:wght@400;700&family=PT+Serif:ital@0;1&family=Open+Sans:wght@400;600&display=swap">
<style>
:root{
  --green:#4f9a1e;
  --green-light:#7cc22c;
  --green-dark:#3c7d12;
  --blue:#3e66a6;
  --blue-dark:#2d4f8a;
  --orange:#e8781a;
  --charcoal:#2c2c2c;
  --grey-card:#dcdcdc;
  --grey-line:#c4c4c4;
  --grey-bg:#ececec;
  --text:#444;
  --white:#fff;
  --footer:#4a6fa8;
}
*{box-sizing:border-box;margin:0;padding:0}
a{text-decoration:none}
html,body{width:1200px;height:2449px;overflow:hidden;background:var(--white);font-family:"Open Sans",sans-serif;color:var(--text)}
.page{position:relative;width:1200px;height:2449px}
.abs{position:absolute}

/* header */
.site-header{left:0;top:0;width:1200px;height:86px;background:var(--white);border-bottom:4px solid var(--green)}
.brand{left:52px;top:18px;font:700 42px/1 "Roboto Slab",serif;color:var(--blue)}
.nav{right:50px;top:40px;display:flex;height:46px}
.nav a{display:block;color:var(--white);font:400 19px/46px "Roboto Slab",serif;padding:0 28px;background:var(--green-dark);border-radius:6px 6px 0 0;margin-left:4px}
.nav a.cta{background:var(--orange);font-weight:700;padding:0 18px}

/* hero */
.hero{left:0;top:86px;width:1200px;height:580px;background:linear-gradient(180deg,#6aa83a 0%,#5da02a 55%,#4d921d 100%)}
.hero h1{left:55px;top:80px;width:900px;font:400 35px/44px "Roboto Slab",serif;color:var(--white);text-transform:uppercase}
.features{left:55px;top:196px;list-style:none}
.features li{position:relative;padding-left:34px;font:400 20px/33px "PT Serif",serif;color:var(--white)}
.features li::before{content:"";position:absolute;left:0;top:8px;width:17px;height:17px;background:var(--orange);border-radius:2px}
.features li::after{content:"";position:absolute;left:4px;top:11px;width:8px;height:5px;border-left:2px solid #fff;border-bottom:2px solid #fff;transform:rotate(-45deg)}
.tagline{left:55px;top:402px;font:italic 400 27px/1 "PT Serif",serif;color:var(--white)}
.btn{display:block;text-align:center;color:var(--white);border-radius:10px;font:400 19px/48px "Roboto Slab",serif;box-shadow:0 3px 0 rgba(0,0,0,.2)}
.btn-blue{left:55px;top:488px;width:160px;background:linear-gradient(#5b83c4,var(--blue-dark))}
.btn-green{left:230px;top:488px;width:182px;background:linear-gradient(#98d845,var(--green-light));font-size:17px}
.laptop{left:528px;top:190px;width:602px;height:340px}
.laptop .bezel{left:0;top:0;width:602px;height:322px;background:#1d1d1d;border-radius:14px}
.laptop .screen{left:16px;top:14px;width:570px;height:296px;background:linear-gradient(135deg,#d7ecf7,#bfe0f1);border-left:22px solid #1fa35a}
.laptop .base{left:-14px;top:322px;width:630px;height:16px;background:linear-gradient(#e4e4e4,#a9a9a9);border-radius:0 0 20px 20px}

/* welcome */
.welcome{left:0;top:666px;width:1200px;height:520px;background:linear-gradient(180deg,#e6e6e6,#f6f6f6 70%,#fbfbfb)}
.welcome-title{left:410px;top:104px;font:400 38px/1 "Roboto Slab",serif;color:#111}
.welcome-text{left:338px;top:190px;width:520px;font:400 14px/21px "Open Sans",sans-serif;color:var(--white)}

/* pricing */
.pricing-title{left:0;top:1222px;width:1200px;text-align:center;font:400 38px/1 "Roboto Slab",serif;color:var(--blue)}
.pricing-intro{left:130px;top:1278px;width:940px;text-align:center;font:400 13px/22px "Open Sans",sans-serif;color:#555}
.plan{top:1370px;width:291px;height:476px;background:var(--grey-card);box-shadow:0 4px 8px rgba(0,0,0,.18)}
.plan-head{height:106px;text-align:center;color:var(--white);font:400 34px/40px "Roboto Slab",serif;padding-top:14px}
.plan-standard{left:135px}.plan-standard .plan-head{background:var(--charcoal)}
.plan-standard .price{color:var(--green-light)}
.plan-premium{left:455px}.plan-premium .plan-head{background:var(--blue)}
.plan-pro{left:775px}.plan-pro .plan-head{background:var(--green)}
.plan ul{list-style:none;padding:0 12px}
.plan li{text-align:center;font:400 13px/16px "Open Sans",sans-serif;color:#333;padding:7px 0;border-bottom:1px solid var(--grey-line)}
.plan li.lead{color:#888;border-bottom:none;padding:12px 0 10px}
.plan li:last-child{border-bottom:none}
.trial{left:435px;top:1890px;width:330px;height:70px;border-radius:12px;background:linear-gradient(#8bcb3a,#4f9a1e);text-align:center;color:var(--white);box-shadow:0 3px 0 rgba(0,0,0,.2)}
.trial small{display:block;font:400 14px/1 "Open Sans",sans-serif;padding-top:11px}
.trial strong{display:block;font:700 27px/1 "Roboto Slab",serif;padding-top:6px}

/* follow */
.follow{left:0;top:2010px;width:1200px;height:236px;background:var(--grey-bg)}
.follow h2{left:0;top:50px;width:1200px;text-align:center;font:400 40px/1 "Roboto Slab",serif;color:#555}
.follow p{left:0;top:100px;width:1200px;text-align:center;font:400 15px/1 "Open Sans",sans-serif;color:#888}
.socials{left:503px;top:145px;display:flex;gap:14px}
.socials span{width:40px;height:40px;border-radius:50%;background:#c9c9c9}

/* subscribe */
.subscribe-title{left:52px;top:2292px;font:400 25px/28px "Roboto Slab",serif;color:#444;text-transform:uppercase}
.field{top:2298px;width:285px;height:50px;border:1px solid #d6d6d6;border-radius:4px;font:400 14px/48px "Open Sans",sans-serif;color:#999;padding-left:14px}
.field-name{left:433px}.field-email{left:728px}
.subscribe-btn{left:1022px;top:2298px;width:126px;height:50px;border-radius:6px;background:linear-gradient(#d9ab3c,#b98418);color:var(--white);font:700 14px/50px "Open Sans",sans-serif;text-align:center}

/* footer */
.site-footer{left:0;top:2390px;width:1200px;height:59px;background:var(--footer);color:#e3eaf5;font:400 13px/59px "Open Sans",sans-serif}
.site-footer .contact{left:52px;top:0;display:flex;gap:44px}
.site-footer .contact span{display:flex;align-items:center;gap:10px}
.site-footer .copy{right:50px;top:0}
</style>
</head>
<body>
<div class="page">

  <header class="site-header abs">
    <div class="brand abs">MoveNest</div>
    <nav class="nav abs">
      <a href="#">Home</a><a href="#">Login</a><a href="#">Help</a><a href="#" class="cta">GET STARTED</a>
    </nav>
  </header>

  <section class="hero abs" role="img" aria-label="Green-tinted photo of a yoga class stretching">
    <h1 class="abs">The easiest way to manage your classes<br>&amp; accept payments online.</h1>
    <ul class="features abs">
      <li>Web based, login anywhere</li>
      <li>Intuitive, easy to use</li>
      <li>Robust, fast and powerful</li>
      <li>Secure, your info is super safe</li>
      <li>Versatile, suitable for any class venue</li>
      <li>Affordable, free version!</li>
    </ul>
    <div class="tagline abs">It's free and installs in 5 minutes</div>
    <a class="btn btn-blue abs" href="#">Learn more</a>
    <a class="btn btn-green abs" href="#">5 MINUTE SETUP!</a>
    <div class="laptop abs">
      <div class="bezel abs"></div>
      <div class="screen abs" role="img" aria-label="App screen illustration listing class types like yoga, dance, karate and music"></div>
      <div class="base abs"></div>
    </div>
  </section>

  <section class="welcome abs" role="img" aria-label="Faded grey photo of a yoga class">
    <svg class="abs" style="left:0;top:0" width="1200" height="520" viewBox="0 0 1200 520">
      <polygon points="335,44 248,174 335,174" fill="#2d4f8a"/>
      <polygon points="250,172 935,172 880,300 318,300" fill="#4a72b5"/>
      <polygon points="790,300 880,300 880,434" fill="#2d4f8a"/>
    </svg>
    <div class="welcome-title abs">Welcome to MoveNest</div>
    <p class="welcome-text abs">MoveNest is the easiest and most affordable way to manage your class studio or venue. We help simplify your daily tasks by leveraging the power of the internet, saving you time and money. Anyone can learn to use MoveNest with our clean, common-sense website.</p>
  </section>

  <h2 class="pricing-title abs">MoveNest Plan &amp; Pricing</h2>
  <p class="pricing-intro abs">Lorem Ipsum is simply dummy text of the printing and typesetting industry. Lorem Ipsum has been the industry's standard dummy text ever since the 1500s, when an unknown printer took a galley of type and scrambled it to make a type specimen book.</p>

  <div class="plan plan-standard abs">
    <div class="plan-head">STANDARD<br><span class="price">Free!</span></div>
    <ul>
      <li class="lead" style="padding:6px 0"></li>
      <li>Fully functional scheduling tool</li>
      <li>Filters for easy viewing</li>
      <li>Web Based: Login Anywhere</li>
      <li>Track students &amp; instructors</li>
      <li>Store/access Customer Info</li>
      <li>Notekeeping &amp; Attendance</li>
      <li>SSL security</li>
      <li>Regular data backups</li>
      <li>1 User account</li>
      <li>E-mail support</li>
      <li>No Credit Card Required</li>
    </ul>
  </div>
  <div class="plan plan-premium abs">
    <div class="plan-head">PREMIUM<br>$39/month</div>
    <ul>
      <li class="lead">Entire Standard Package, plus....</li>
      <li>3 User Accounts</li>
      <li>Simultaneous Logins</li>
      <li>Collaboration: File Sharing &amp; Storage</li>
      <li>Activity Feed: Track your efforts</li>
      <li>Activity Feed: Discussion Board</li>
      <li>Reports: Attendance Sheets</li>
      <li>Reports: Instructor Work Histories &amp; Schedules</li>
      <li>Reports: Customer Histories &amp; Schedules</li>
      <li>Best in Class Phone Support</li>
    </ul>
  </div>
  <div class="plan plan-pro abs">
    <div class="plan-head">PROFESSIONAL<br>$79/month</div>
    <ul>
      <li class="lead">Entire Standard Package, plus....</li>
      <li>Powerful Point of Sale System</li>
      <li>Accept Credit Cards Immediately</li>
      <li>Web Store: Sell Your Classes Online</li>
      <li>Easily Publish Your Schedule Online</li>
      <li>Sell Retail Goods, Tickets, and More</li>
      <li>Postwren Integration</li>
      <li>LedgerPro Integration</li>
      <li>Add User Accounts for $5</li>
      <li>Priority Customer Support</li>
    </ul>
  </div>

  <a class="trial abs" href="#"><small>Ask about a free 30 days trial!</small><strong>GET START TODAY</strong></a>

  <section class="follow abs">
    <h2 class="abs">Follow us</h2>
    <p class="abs">Stay connected with us on Chatterly and Pinwire</p>
    <div class="socials abs"><span></span><span></span><span></span><span></span></div>
  </section>

  <div class="subscribe-title abs">Subscribe to our<br>newsletter</div>
  <div class="field field-name abs">Your name</div>
  <div class="field field-email abs">Email_address</div>
  <div class="subscribe-btn abs">SUBSCRIBE</div>

  <footer class="site-footer abs">
    <div class="contact abs">
      <span><svg width="18" height="14" viewBox="0 0 18 14"><path d="M1 5c0-3 16-3 16 0v2h-4V5H5v2H1z M4 8h10l2 5H2z" fill="#e3eaf5"/></svg>Phone: 0123456789</span>
      <span><svg width="16" height="12" viewBox="0 0 16 12"><rect x="0.5" y="0.5" width="15" height="11" fill="none" stroke="#e3eaf5"/><path d="M1 1l7 6 7-6" fill="none" stroke="#e3eaf5"/></svg>Email: info@movenest.com</span>
    </div>
    <div class="copy abs">Copyright © 2014. MoveNest | All Right Reserved.</div>
  </footer>

</div>
</body>
</html>
```